Hottest Internet Based Blues Radio Station in Southwest Florida All Blues 24/7 Real Authentic Blues Classic and Modern

Business

Marco "Tall Ned" Okafor
The Harbor Airwaves, Inc.
514 Willow Crest Lane
Cedar Cove, GA 33871

```html
<!DOCTYPE html>
<html lang="en">
<head>
<meta charset="utf-8">
<title>Harbor Airwaves – Business Card</title>
<link rel="stylesheet" href="https://fonts.googleapis.com/css2?family=Kurale&family=Oswald:wght@500&display=swap">
<style>
  :root {
    --page: #ffffff;
    --card: #0f1012;
    --ink: #f4f1ec;
    --ghost: #222326;
    --ring: #d9d4cc;
  }
  * { margin: 0; padding: 0; box-sizing: border-box; }
  html, body { width: 1200px; height: 782px; overflow: hidden; background: var(--page); }
  .canvas { position: relative; width: 1200px; height: 782px; }
  .card {
    position: absolute; left: 288px; width: 644px; height: 358px;
    background: var(--card); overflow: hidden;
  }
  .card--front { top: 22px; }
  .card--back { top: 404px; }

  .brand {
    position: absolute; left: 0; right: 0; top: 120px;
    display: flex; flex-direction: column; align-items: center; gap: 26px;
  }
  .brand__ring { width: 86px; height: 86px; }
  .brand__name {
    font-family: "Kurale", serif; font-size: 40px; color: var(--ink);
    letter-spacing: 2px; line-height: 1;
  }

  .motto {
    position: absolute; left: 26px; top: 222px;
    font-family: "Oswald", sans-serif; font-weight: 500; font-size: 54px;
    line-height: 1.05; color: var(--ghost); text-transform: uppercase;
    letter-spacing: 1px;
  }
  .motto span { display: block; }
  .motto span:nth-child(2) { padding-left: 34px; }

  .person {
    position: absolute; left: 0; right: 0; top: 128px; text-align: center;
    font-family: "Kurale", serif; color: var(--ink);
  }
  .person__name { font-size: 47px; font-weight: 400; line-height: 1.1; }
  .person__company { font-size: 20px; margin-top: 2px; }

  .address {
    position: absolute; right: 23px; bottom: 18px; text-align: right;
    font-family: "Kurale", serif; font-style: normal;
    font-size: 21px; line-height: 35px; color: var(--ink);
  }
</style>
</head>
<body>
<main class="canvas">
  <section class="card card--front">
    <div class="brand">
      <svg class="brand__ring" viewBox="0 0 86 86" aria-hidden="true">
        <circle cx="43" cy="43" r="41" fill="none" stroke="var(--ring)" stroke-width="2"/>
      </svg>
      <div class="brand__name">HARBOR AIRWAVES</div>
    </div>
  </section>

  <section class="card card--back">
    <div class="motto" aria-hidden="true">
      <span>All Blues</span>
      <span>24/7</span>
    </div>
    <div class="person">
      <h1 class="person__name">Marco "Tall Ned" Okafor</h1>
      <p class="person__company">The Harbor Airwaves, Inc.</p>
    </div>
    <address class="address">
      514 Willow Crest Lane<br>
      Cedar Cove, GA 33871
    </address>
  </section>
</main>
</body>
</html>
```